3D Scans and Virtual Tour photography company needs a website

We need a website build that explains what we do, shows some examples of our 3d scans and virtual tours, some stats on why they are important when when selling your home or marketing your business/premises and a contact form to find out more. We need to target both the real estate agents and consumers. The site needs to looks modern, engaging, clean, not lots of text but more pictures and icons. Needs to be mobile friendly. In fact i would build it from the mobile then out.

Reason: Hi Team, I have had a couple of requests to extend the Project deadline, which I have now done. I cant push it much more than this as the business is up and running now and I need the website. Looking forward to reviewing the designs.

Target Market(s)

people selling their home and the real estate industry mostly, however any building can be scanned and have a 3d tour

Industry/Entity Type

Photographer

Font styles to use
Sans Serif

Colors
32a6d6
0355a3
33a6d7
85cae6
cee9f5
3176b5

Requirements
Must have
• Our logo
• an example of the 3d scans
• an example of a dollhouse view
• a contact page
• Replace the orange document examples to blue please
• social media links Friendloop Snapgrid Chirpline
Nice to have
• some examples of similar companies websites we like
• favourite would be this one brindlenook (dot com)
• next fav roomvale (dot com au) and wexlorn (dot com au)

```html
<!DOCTYPE html>
<html lang="en">
<head>
<meta charset="utf-8">
<title>LUMIVEX Imagery</title>
<link href="https://fonts.googleapis.com/css2?family=Roboto:wght@400;500;700&family=Roboto+Condensed:wght@500;700&display=swap" rel="stylesheet">
<style>
:root{
  --blue:#32a6d6;
  --navy:#0355a3;
  --mid:#3176b5;
  --light:#85cae6;
  --pale:#cee9f5;
  --ink:#2b2b2b;
  --text:#555;
  --grey-bg:#f4f4f4;
  --footer:#1d1d1d;
  --white:#fff;
}
*{box-sizing:border-box;margin:0;padding:0}
html,body{width:1200px;height:3267px;overflow:hidden}
body{font-family:"Roboto",Arial,sans-serif;color:var(--ink);background:var(--white);position:relative}
a{color:inherit;text-decoration:none}

/* header */
.site-header{position:absolute;left:0;top:0;width:1200px;height:118px;background:var(--white)}
.brand{position:absolute;left:98px;top:24px;display:flex;align-items:center;gap:12px}
.brand-mark{width:22px;height:22px;border-radius:50%;background:var(--mid)}
.brand-name{font-size:40px;font-weight:700;color:var(--mid);letter-spacing:1px;line-height:1}
.top-contact{position:absolute;top:22px;right:98px;display:flex;gap:36px;font-size:15px;color:#444}
.top-contact span{display:flex;align-items:center;gap:10px}
.icon-dot{width:26px;height:26px;border-radius:50%;background:var(--mid);display:flex;align-items:center;justify-content:center}
.main-nav{position:absolute;right:98px;top:76px;display:flex;gap:28px;font-size:13px;font-weight:500;color:#333}
.main-nav a{padding-bottom:14px}
.main-nav a.active{color:var(--blue);border-bottom:2px solid var(--blue)}

/* hero */
.hero{position:absolute;left:0;top:118px;width:1200px;height:540px;background:linear-gradient(180deg,#6f7c86 0%,#7d7464 45%,#4f5b3a 80%,#3e4a2c 100%)}
.hero-shade{position:absolute;inset:0;background:linear-gradient(90deg,rgba(0,0,0,.45),rgba(0,0,0,.1))}
.hero-title{position:absolute;left:98px;top:200px;font-family:"Roboto Condensed",sans-serif;font-weight:500;font-size:40px;line-height:1.1;color:var(--white)}
.hero-sub{position:absolute;left:98px;top:296px;width:330px;font-size:14px;line-height:1.5;color:var(--white)}
.hero-dots{position:absolute;left:98px;top:356px;display:flex;gap:8px}
.hero-dots i{width:12px;height:12px;border-radius:50%;background:var(--white)}
.hero-dots i.on{box-shadow:0 0 0 3px rgba(255,255,255,.5)}

/* process */
.section-title{position:absolute;left:0;width:1200px;text-align:center;font-size:30px;font-weight:400}
.process-title{top:714px}
.process-title b{color:var(--mid);font-weight:500}
.step{position:absolute;width:240px;text-align:center}
.step-ring{width:150px;height:150px;margin:0 auto;border-radius:50%;border:2px dashed #9fd3ea;padding:6px}
.step-ring div{width:100%;height:100%;border-radius:50%;background:var(--blue);display:flex;align-items:center;justify-content:center}
.step h3{font-size:18px;font-weight:400;margin-top:22px;color:#333}
.step p{font-size:12.5px;color:var(--text);margin-top:8px}
.step-arrow{position:absolute;font-size:14px;color:#333;text-align:center}

/* features */
.features{position:absolute;left:0;top:1115px;width:1200px;height:464px;background:linear-gradient(180deg,#2a6cc2 0%,#1b5fb4 60%,#2466b0 100%)}
.features-photo{position:absolute;left:122px;top:96px;width:462px;height:277px;border:4px solid var(--white);background:linear-gradient(180deg,#9fb6c9 0%,#8c9a8a 45%,#5e8a3e 80%,#4f7a34 100%)}
.play{position:absolute;left:209px;top:116px;width:46px;height:46px;border-radius:50%;border:3px solid rgba(255,255,255,.85)}
.deg{position:absolute;right:26px;bottom:26px;color:var(--white);font-size:22px;text-align:center}
.features-body{position:absolute;left:625px;top:112px;width:480px;color:var(--white)}
.features-body h2{font-size:29px;font-weight:400}
.features-body p{font-size:11.5px;line-height:1.6;margin-top:18px}
.features-body ul{list-style:none;margin-top:14px}
.features-body li{font-size:13px;line-height:26px;display:flex;align-items:center;gap:12px}
.features-body li:before{content:"";width:9px;height:9px;border-radius:50%;background:var(--white)}

/* benefits */
.benefits-title{top:1652px;font-weight:500;letter-spacing:.5px}
.benefit{position:absolute;width:240px;text-align:center}
.benefit-ring{width:106px;height:106px;margin:0 auto;border-radius:50%;border:1.5px solid var(--navy);display:flex;align-items:center;justify-content:center}
.benefit h3{font-size:17px;font-weight:400;margin-top:16px;color:#333}
.benefit p{font-size:12px;line-height:1.6;color:var(--text);margin-top:6px}
.benefit .chev{margin-top:14px}

/* virtual tours */
.tours{position:absolute;left:0;top:2069px;width:1200px;height:436px;background:var(--grey-bg)}
.tours-image{position:absolute;left:148px;top:76px;width:331px;height:299px;background:radial-gradient(ellipse at 50% 55%,#c9cdd1 0%,#b5bcc4 40%,rgba(244,244,244,0) 72%)}
.tours-body{position:absolute;left:538px;top:100px;width:560px}
.tours-body h2{font-size:28px;font-weight:500;color:#333}
.tours-body p{font-size:12px;line-height:1.75;color:var(--text);margin-top:16px}
.btn-outline{display:inline-block;margin-top:30px;border:1.5px solid #777;padding:9px 16px;font-size:12px;color:#444}

/* blog */
.blog-title{position:absolute;left:98px;top:2572px;font-size:28px;font-weight:500;color:#333}
.blog-nav{position:absolute;left:1076px;top:2578px;font-size:20px;color:#444;letter-spacing:8px}
.post-img{position:absolute;width:214px;height:170px}
.post-body{position:absolute;width:260px}
.post-body h3{font-size:17px;font-weight:400;color:#333}
.date{display:inline-block;background:var(--blue);color:var(--white);font-size:12px;font-weight:500;font-style:italic;padding:5px 10px;margin-top:14px}
.post-body p{font-size:12px;line-height:1.6;color:var(--text);margin-top:12px}
.post-body a{display:block;color:var(--blue);font-size:13px;margin-top:12px}

/* footer */
.site-footer{position:absolute;left:0;top:2897px;width:1200px;height:370px;background:var(--footer);color:#ddd}
.f-brand{position:absolute;left:98px;top:66px;display:flex;align-items:center;gap:10px}
.f-brand .brand-name{font-size:34px}
.f-address{position:absolute;left:98px;top:140px;font-size:13px;line-height:1.6}
.f-line{position:absolute;left:98px;font-size:13px;display:flex;align-items:center;gap:12px}
.f-head{position:absolute;top:68px;font-size:15px;font-weight:500;color:#fff;letter-spacing:.3px}
.f-news p{position:absolute;left:429px;top:108px;width:250px;font-size:12px;line-height:1.6}
.f-input{position:absolute;left:429px;top:155px;width:244px;height:42px;background:#fff;color:#777;font-size:12px;padding:13px 14px}
.f-btn{position:absolute;left:429px;top:210px;width:122px;height:32px;background:var(--blue);color:#fff;font-size:12px;font-weight:500;display:flex;align-items:center;justify-content:center}
.f-links{position:absolute;left:791px;top:110px;list-style:none;font-size:12px}
.f-links li{line-height:23px;display:flex;align-items:center;gap:14px}
.f-links li:before{content:"";width:9px;height:9px;border-radius:50%;background:#eee}
.f-social{position:absolute;left:991px;top:104px;list-style:none;font-size:14px}
.f-social li{display:flex;align-items:center;gap:12px;height:36px}
.f-social li i{width:26px;height:26px;border-radius:50%;border:1.5px solid #ddd}
.f-rule{position:absolute;left:0;top:305px;width:1200px;height:1px;background:#333}
.f-copy{position:absolute;left:0;top:332px;width:1200px;text-align:center;font-size:12px;color:#ccc}
</style>
</head>
<body>

<header class="site-header">
  <div class="brand"><span class="brand-mark"></span><span class="brand-name">LUMIVEX</span></div>
  <div class="top-contact">
    <span><i class="icon-dot"><svg width="13" height="13" viewBox="0 0 24 24"><path fill="#fff" d="M6.6 10.8a15 15 0 0 0 6.6 6.6l2.2-2.2c.3-.3.7-.4 1-.2 1.1.4 2.3.6 3.6.6.6 0 1 .4 1 1V20c0 .6-.4 1-1 1A17 17 0 0 1 3 4c0-.6.4-1 1-1h3.5c.6 0 1 .4 1 1 0 1.3.2 2.5.6 3.6.1.3 0 .7-.2 1z"/></svg></i>(555) 310-4482</span>
    <span><i class="icon-dot"><svg width="13" height="13" viewBox="0 0 24 24"><path fill="#fff" d="M3 5h18v14H3z M3 5l9 7 9-7" stroke="#3176b5" stroke-width="1.5"/></svg></i>info@lumivex.com.au</span>
  </div>
  <nav class="main-nav">
    <a class="active">HOME</a><a>ABOUT US</a><a>OUR SERVICES</a><a>PARTNERSHIPS</a><a>BLOG</a><a>CONTACT US</a>
  </nav>
</header>

<section class="hero" role="img" aria-label="Photo of a two-storey timber house with porch, front lawn and trees">
  <div class="hero-shade"></div>
  <h1 class="hero-title">REAL ESTATE<br>VALUE PROPOSITION</h1>
  <p class="hero-sub">Sed ut perspiciatis unde omnis iste natus error sit voluptatem accusantium doloremque</p>
  <div class="hero-dots"><i class="on"></i><i></i><i></i><i></i></div>
</section>

<h2 class="section-title process-title"><b>LUMIVEX</b> Process</h2>
<div class="step" style="left:130px;top:811px">
  <div class="step-ring"><div><svg width="60" height="60" viewBox="0 0 24 24" fill="none" stroke="#fff" stroke-width="1.3"><rect x="3" y="7" width="18" height="13" rx="2"/><path d="M8 7l1.5-3h5L16 7"/><circle cx="12" cy="13.5" r="3.5"/></svg></div></div>
  <h3>Scan</h3><p>Capture a space in 3d</p>
</div>
<div class="step-arrow" style="left:380px;top:858px">2 hrs<br><svg width="74" height="24" viewBox="0 0 74 24"><path d="M2 18 Q36 2 68 12" fill="none" stroke="#333" stroke-width="1.5" stroke-dasharray="4 4"/><path d="M62 7l7 5-8 3" fill="none" stroke="#333" stroke-width="1.5"/></svg></div>
<div class="step" style="left:481px;top:811px">
  <div class="step-ring"><div><svg width="60" height="60" viewBox="0 0 24 24" fill="none" stroke="#fff" stroke-width="1.3"><path d="M7 18H6a4 4 0 0 1-.5-8A6 6 0 0 1 17 8.5 4.8 4.8 0 0 1 18 18h-1"/><path d="M12 20v-8M9 14.5l3-3 3 3"/></svg></div></div>
  <h3>Upload</h3><p>Process&amp; store in the cloud</p>
</div>
<div class="step-arrow" style="left:752px;top:906px"><svg width="74" height="24" viewBox="0 0 74 24"><path d="M2 8 Q36 24 68 10" fill="none" stroke="#333" stroke-width="1.5" stroke-dasharray="4 4"/><path d="M61 6l8 4-6 6" fill="none" stroke="#333" stroke-width="1.5"/></svg><br>48 hrs</div>
<div class="step" style="left:830px;top:811px">
  <div class="step-ring"><div><svg width="60" height="60" viewBox="0 0 24 24" fill="none" stroke="#fff" stroke-width="1.3"><rect x="7" y="2.5" width="10" height="19" rx="1.5"/><path d="M7 5.5h10M7 18h10"/><circle cx="12" cy="19.8" r=".6" fill="#fff"/></svg></div></div>
  <h3>View</h3><p>Experience via web &amp; mobile</p>
</div>

<section class="features" role="img" aria-label="Blue-tinted photo of a house on a green lawn under a sky">
  <div class="features-photo" role="img" aria-label="Video still of a suburban street with houses and lawns">
    <div class="play"><svg width="40" height="40" viewBox="0 0 40 40"><path d="M16 12l12 8-12 8z" fill="rgba(255,255,255,.9)"/></svg></div>
    <div class="deg">360°<br><svg width="80" height="26" viewBox="0 0 80 26"><ellipse cx="40" cy="13" rx="36" ry="9" fill="none" stroke="#fff" stroke-width="2"/><path d="M70 6l6 7-8 2" fill="none" stroke="#fff" stroke-width="2"/></svg></div>
  </div>
  <div class="features-body">
    <h2>LUMIVEX Features</h2>
    <p>Sed ut perspiciatis unde omnis iste natus error sit voluptatem accusantium doloremque laudantium, totam rem aperiam, eaque ipsa quae ab illo inventore veritatis et quasi architecto beatae vitae dicta sunt explicabo. Nemo enim ipsam</p>
    <ul>
      <li>3D Tour (integrated into all portals)</li>
      <li>Traditional floor plan (with measurements)</li>
      <li>Company branding and digital presence</li>
      <li>Fortnightly analytic reports</li>
      <li>Leading web integration and backend support</li>
    </ul>
  </div>
</section>

<h2 class="section-title benefits-title">OUR BENEFITS</h2>
<div class="benefit" style="left:83px;top:1750px">
  <div class="benefit-ring"><svg width="46" height="46" viewBox="0 0 24 24"><path d="M5 3h10l4 4v14H5z" fill="#0355a3"/><path d="M8 10h8M8 13h8M8 16h5" stroke="#fff" stroke-width="1.2"/><path d="M14 20l7-7 1.5 1.5-7 7H14z" fill="#0355a3" stroke="#fff" stroke-width=".8"/></svg></div>
  <h3>High Conversion</h3><p>Sed ut perspiciatis unde omnis iste natus error sit voluptatem accusantium dolque laudantium, totam rem</p>
  <div class="chev"><svg width="16" height="16" viewBox="0 0 16 16" fill="none" stroke="#444" stroke-width="1.5"><path d="M3 3l5 5 5-5M3 8l5 5 5-5"/></svg></div>
</div>
<div class="benefit" style="left:346px;top:1750px">
  <div class="benefit-ring"><svg width="46" height="46" viewBox="0 0 24 24" fill="#0355a3"><circle cx="12" cy="8" r="4"/><path d="M4 21c0-4.4 3.6-7 8-7s8 2.6 8 7z"/></svg></div>
  <h3>Greater Engagement</h3><p>Sed ut perspiciatis unde omnis iste natus error sit voluptatem accusantium dolque laudantium, totam rem</p>
  <div class="chev"><svg width="16" height="16" viewBox="0 0 16 16" fill="none" stroke="#444" stroke-width="1.5"><path d="M3 3l5 5 5-5M3 8l5 5 5-5"/></svg></div>
</div>
<div class="benefit" style="left:607px;top:1750px">
  <div class="benefit-ring"><svg width="46" height="46" viewBox="0 0 24 24" fill="none" stroke="#0355a3" stroke-width="1.4"><circle cx="12" cy="10" r="7"/><path d="M5 10h14M12 3c2.5 2.5 2.5 11.5 0 14M12 3c-2.5 2.5-2.5 11.5 0 14"/><path d="M3 17c3 3 7 4 11 3l6-3" stroke-width="2"/></svg></div>
  <h3>Worldwide Appeal</h3><p>Sed ut perspiciatis unde omnis iste natus error sit voluptatem accusantium dolque laudantium, totam rem</p>
  <div class="chev"><svg width="16" height="16" viewBox="0 0 16 16" fill="none" stroke="#444" stroke-width="1.5"><path d="M3 3l5 5 5-5M3 8l5 5 5-5"/></svg></div>
</div>
<div class="benefit" style="left:871px;top:1750px">
  <div class="benefit-ring"><svg width="46" height="46" viewBox="0 0 24 24" fill="#0355a3"><path d="M11 4a8 8 0 1 0 8 9h-8z"/><path d="M13 2v9h9a9 9 0 0 0-9-9z"/></svg></div>
  <h3>Boost Traffic</h3><p>Sed ut perspiciatis unde omnis iste natus error sit voluptatem accusantium dolque laudantium, totam rem</p>
  <div class="chev"><svg width="16" height="16" viewBox="0 0 16 16" fill="none" stroke="#444" stroke-width="1.5"><path d="M3 3l5 5 5-5M3 8l5 5 5-5"/></svg></div>
</div>

<section class="tours">
  <div class="tours-image" role="img" aria-label="Illustration of a white model house with a grey roof and red shutters"></div>
  <div class="tours-body">
    <h2>VIRTUAL TOURS</h2>
    <p>Nemo enim ipsam voluptatem quia voluptas sit aspernatur aut odit aut fugit, sed quia consequuntur magni dolores eos qui ratione voluptatem sequi nesciunt. Neque porro quisquam est, qui dolorem ipsum quia dolor sit amet, consectetur, adipisci velit, sed quia non numquam eius modi tempora incidunt ut labore et dolore magnam aliquam quaerat voluptatem.</p>
    <p>Nemo enim ipsam voluptatem quia voluptas sit aspernatur aut odit aut fugit, sed quia consequuntur magni dolores eos qui ratione voluptatem sequi nesciunt.</p>
    <a class="btn-outline">READ MORE ⊕</a>
  </div>
</section>

<h2 class="blog-title">LATEST BLOG</h2>
<div class="blog-nav">‹›</div>
<div class="post-img" style="left:98px;top:2644px;background:linear-gradient(180deg,#a9c4de 0%,#c9c3b4 45%,#6d8a52 100%)" role="img" aria-label="Photo of a large suburban family home with garden"></div>
<div class="post-body" style="left:338px;top:2645px">
  <h3>Lorem ipsum dolor sit amet</h3>
  <span class="date">April 26, 2017</span>
  <p>Lorem ipsum dolor sit amet, consectetur adipiscing elit, uspendisse id erat sit amet ante interdum suscipit eget</p>
  <a>Learn More</a>
</div>
<div class="post-img" style="left:647px;top:2644px;background:linear-gradient(180deg,#4f86c8 0%,#d9c27d 50%,#7c9a5a 100%)" role="img" aria-label="Photo of a yellow two-storey house with a garage"></div>
<div class="post-body" style="left:884px;top:2645px">
  <h3>Lorem ipsum dolor sit amet</h3>
  <span class="date">April 26, 2017</span>
  <p>Lorem ipsum dolor sit amet, consectetur adipiscing elit, uspendisse id erat sit amet ante interdum suscipit eget</p>
  <a>Learn More</a>
</div>

<footer class="site-footer">
  <div class="f-brand"><span class="brand-mark"></span><span class="brand-name">LUMIVEX</span></div>
  <p class="f-address">LUMIVEX<br>Ashgrove Lane Ferndale, GA 30199</p>
  <div class="f-line" style="top:190px"><svg width="18" height="18" viewBox="0 0 24 24"><path fill="none" stroke="#ddd" stroke-width="1.6" d="M6.6 10.8a15 15 0 0 0 6.6 6.6l2.2-2.2 4.6 1.4V20A17 17 0 0 1 3 4h3.8l1.4 4.6z"/></svg>Phone: (555) 720-1194</div>
  <div class="f-line" style="top:224px"><svg width="18" height="18" viewBox="0 0 24 24" fill="none" stroke="#ddd" stroke-width="1.6"><rect x="3" y="5" width="18" height="14"/><path d="M3 5l9 7 9-7"/></svg>Email: info@lumivex.com.au</div>

  <h4 class="f-head" style="left:429px">SIGN UP FOR NEWSLETTER</h4>
  <div class="f-news"><p>Excepteur sint occaecat cupidatat non proident, sunt in culpa qui officia deserunt</p></div>
  <div class="f-input">Enter email</div>
  <div class="f-btn">SUBSCRIPTION</div>

  <h4 class="f-head" style="left:791px">QUICK LINKS</h4>
  <ul class="f-links"><li>Home</li><li>About Us</li><li>Our Project</li><li>Service</li><li>Blog</li><li>Contact Us</li></ul>

  <h4 class="f-head" style="left:991px">SOCIAL MEDIA</h4>
  <ul class="f-social"><li><i></i>Friendloop</li><li><i></i>Chirpline</li><li><i></i>Snapgrid</li></ul>

  <div class="f-rule"></div>
  <p class="f-copy">©2017 LUMIVEX, All Rights Reserved.</p>
</footer>

</body>
</html>
```